Book Cover For Velvet Canyon Echoes

Need a book cover design to incorporate the following elements, which are attached. Size should be 6.125 x 9.25 niches. Explanation of attachments: 1) I drew up a sketch for the concept. 2) the artistic style from the Bali book would be preferable but not necessary. 3) I posted some images on a word doc to help create a visual of elements to include and some colors...the top image of the surfer on the word doc is a perfect style to copy. Also included at the bottom of the word doc are several images with color possibilities that can be experimented with. 4) Ideally, the font would be the golden encrusted royal font attached.
- all specifics are indicated on the rough sketch and images that are attached.

```html
<!DOCTYPE html>
<html lang="en">
<head>
<meta charset="utf-8">
<title>Velvet Canyon Echoes – Book Cover</title>
<link href="https://fonts.googleapis.com/css2?family=Cinzel:wght@400;700;900&display=swap" rel="stylesheet">
<style>
  :root {
    --stage: #e9e9ea;
    --navy: #231a5c;
    --gold: #e2c77a;
    --gold-deep: #b8923e;
    --lavender: #d8d2e6;
    --ink: #1f1a4a;
    --sky-magenta: #e0407e;
    --sky-pink: #f46a8c;
    --sky-orange: #f89a5c;
    --horizon: #f5b6a8;
    --sea-teal: #3d9aa2;
    --sea-deep: #2a6f86;
    --shore: #4fa59a;
    --sand: #cda53e;
    --sand-deep: #b07a2c;
  }
  * { box-sizing: border-box; margin: 0; padding: 0; }
  html, body {
    width: 1200px;
    height: 800px;
    overflow: hidden;
    background: var(--stage);
  }
  .stage {
    width: 1200px;
    height: 800px;
    display: flex;
    align-items: center;
    justify-content: center;
  }
  .cover {
    position: relative;
    width: 490px;
    height: 740px;
    overflow: hidden;
    box-shadow: 0 6px 18px rgba(0,0,0,0.25);
  }
  .cover-art {
    position: absolute;
    inset: 0;
    background:
      radial-gradient(ellipse 40% 22% at 8% 22%, rgba(90,60,170,0.85), transparent 70%),
      linear-gradient(180deg,
        var(--sky-magenta) 0%,
        var(--sky-pink) 22%,
        var(--sky-orange) 38%,
        var(--horizon) 47%,
        var(--sea-teal) 53%,
        var(--sea-deep) 64%,
        var(--shore) 76%,
        var(--sky-pink) 80%,
        var(--sand) 85%,
        var(--sand-deep) 100%);
  }
  .title-panel {
    position: absolute;
    top: 0;
    left: 17%;
    width: 65.6%;
    height: 33.5%;
    background: var(--navy);
    display: flex;
    flex-direction: column;
    align-items: center;
    padding-top: 46px;
    box-shadow: 0 3px 8px rgba(0,0,0,0.3);
  }
  .book-title {
    font-family: "Cinzel", serif;
    font-weight: 900;
    font-size: 40px;
    line-height: 1.02;
    text-align: center;
    color: var(--gold);
    letter-spacing: 0.5px;
    text-shadow: 0 2px 0 var(--gold-deep);
  }
  .title-rule {
    width: 82%;
    height: 1px;
    background: var(--gold-deep);
    margin: 14px 0 9px;
  }
  .book-subtitle {
    font-family: "Cinzel", serif;
    font-weight: 400;
    font-size: 16px;
    line-height: 1.45;
    text-align: center;
    color: var(--gold);
    letter-spacing: 0.4px;
  }
  .author-plate {
    position: absolute;
    left: 30.5%;
    bottom: 0;
    width: 39%;
    height: 8.6%;
    background: var(--lavender);
    display: flex;
    align-items: center;
    justify-content: center;
  }
  .author-name {
    font-family: "Cinzel", serif;
    font-weight: 700;
    font-size: 16px;
    color: var(--ink);
    letter-spacing: 0.6px;
  }
</style>
</head>
<body>
  <main class="stage">
    <section class="cover">
      <div class="cover-art" role="img" aria-label="Painterly textured beach at sunset: pink and orange sky with seabirds, a surfer on teal waves, a blue beach umbrella and a figure on a lounge chair on golden sand"></div>
      <header class="title-panel">
        <h1 class="book-title">Velvet Canyon<br>Echoes</h1>
        <div class="title-rule"></div>
        <p class="book-subtitle">Four seasons to hear what<br>the stone remembers</p>
      </header>
      <footer class="author-plate">
        <p class="author-name">Harold Brenner</p>
      </footer>
    </section>
  </main>
</body>
</html>
```